School Poster

Design so that these can be placed in classrooms across the school.

Attached is another design we have had done. Use a similar theme.

Consider using themes from https://calderwoodhs.lumorin.edu/

please edit Binder1 doc.

Target Market(s)

Students and teachers

```html
<!DOCTYPE html>
<html lang="en">
<head>
<meta charset="utf-8">
<title>Before You Ask the Teacher – Calderwood State High School</title>
<link href="https://fonts.googleapis.com/css2?family=Roboto+Condensed:ital,wght@0,400;0,700;1,700&family=Roboto:wght@400;500;700&family=Kaushan+Script&display=swap" rel="stylesheet">
<style>
:root{
  --navy:#0e3d86;
  --ink:#1b2549;
  --gold:#f8c220;
  --paper:#f6f7fb;
  --mist:#e8eef8;
  --green:#246a2e;
  --red:#c9161e;
  --lilac:#eef0fa;
  --text:#1c2238;
  --white:#ffffff;
}
*{box-sizing:border-box;margin:0;padding:0}
html,body{width:848px;height:1200px;overflow:hidden;background:var(--white)}
body{position:relative;font-family:"Roboto",sans-serif;color:var(--text)}
.abs{position:absolute}
.backdrop{position:absolute;left:0;top:0}

/* header */
.brand{left:40px;top:44px;width:160px;text-align:center}
.brand-mark{width:84px;height:84px;background:var(--navy);margin:0 auto 12px;border-radius:4px}
.brand-name{font-family:"Roboto Condensed",sans-serif;font-weight:700;color:var(--navy);font-size:22px;line-height:1.05;letter-spacing:.5px}
.header-rule{left:230px;top:37px;width:2px;height:188px;background:var(--navy)}
.title{left:254px;top:38px;font-family:"Roboto Condensed",sans-serif;font-weight:700;line-height:.98;font-size:62px;letter-spacing:.3px}
.title .line1{color:var(--navy);display:block}
.title .line2{color:var(--gold);display:block;margin-top:4px}
.steps-banner{left:276px;top:186px;width:356px;height:40px;background:var(--navy);clip-path:polygon(4% 0,100% 0,96% 100%,0 100%);display:flex;align-items:center;justify-content:center}
.steps-banner span{font-family:"Roboto Condensed",sans-serif;font-style:italic;font-weight:700;color:var(--white);font-size:29px;letter-spacing:.3px}
.deco{border-radius:50%}

/* step cards */
.card{position:absolute;top:280px;height:377px;background:var(--paper);border:1.5px solid var(--gold);border-radius:18px}
.card-icon{position:absolute;top:-48px;width:104px;height:104px;margin-left:-52px;border-radius:50%;background:var(--white);box-shadow:0 2px 6px rgba(20,30,70,.18);display:flex;align-items:center;justify-content:center}
.card-icon .disc{width:88px;height:88px;border-radius:50%;background:var(--ink);display:flex;align-items:center;justify-content:center}
.step-tab{position:absolute;left:-1px;top:16px;width:58px;height:37px;background:var(--ink);clip-path:polygon(0 0,62% 0,100% 100%,0 100%);color:var(--white);font-family:"Roboto Condensed",sans-serif;font-weight:700;font-size:21px;padding:5px 0 0 20px}
.card h2{position:absolute;top:64px;left:0;right:0;text-align:center;font-family:"Roboto Condensed",sans-serif;font-weight:700;font-size:20px;color:var(--ink);letter-spacing:.2px}
.card .lead{position:absolute;top:96px;left:0;right:0;text-align:center;font-family:"Roboto Condensed",sans-serif;font-size:15px;color:var(--ink)}
.card .dash{position:absolute;left:30px;right:22px;top:124px;border-top:1.5px dashed #8a90a8}
.checklist{position:absolute;list-style:none}
.checklist li{display:flex;align-items:center;gap:6px;height:35.3px;font-size:11.4px;color:var(--text)}
.tick{flex:0 0 24px;width:24px;height:24px}
.card-foot{position:absolute;left:1px;right:1px;bottom:1px;height:58px;background:var(--ink);border-radius:0 0 16px 16px;display:flex;align-items:center;justify-content:center;gap:22px}
.card-foot span{font-family:"Roboto Condensed",sans-serif;font-weight:700;font-size:20px;color:var(--white)}

.card-ask .lead{text-align:left;left:40px;line-height:14px;top:96px}
.card-ask .dash{top:135px;left:30px}
.card-ask .checklist li.tall{height:52px;align-items:flex-start;padding-top:6px;line-height:20px}
.card-ask .rule{position:absolute;left:18px;right:22px;top:275px;border-top:1px solid #9aa0b4}
.card-ask .then{position:absolute;left:39px;top:282px;font-family:"Roboto Condensed",sans-serif;font-weight:700;font-size:13.5px;line-height:16px;color:var(--ink)}

/* AI section */
.ai-banner{left:144px;top:681px;width:536px;height:72px;background:var(--ink);clip-path:polygon(0 0,100% 0,93% 50%,100% 100%,0 100%,7% 50%)}
.ai-title{left:144px;top:688px;width:536px;text-align:center;font-family:"Roboto Condensed",sans-serif;font-weight:700;font-size:28px;color:var(--white);letter-spacing:.4px}
.ai-title .chev{color:var(--white);font-size:22px;margin:0 12px;font-weight:400;vertical-align:2px}
.ai-script{left:340px;top:712px;width:150px;text-align:center;font-family:"Kaushan Script",cursive;color:var(--gold);font-size:25px}
.ai-panel{left:35px;top:752px;width:778px;height:366px;background:var(--white);border-radius:36px}
.ai-visual{left:347px;top:752px;width:143px;height:236px;background:radial-gradient(circle at 55% 45%,#5fb7e6 0,#23507e 30%,#0f1f3f 75%)}

.rule-box{position:absolute;top:790px;height:188px;width:297px;background:var(--lilac);border:1.5px solid var(--ink);border-radius:14px}
.rule-head{position:absolute;top:763px;height:45px;border-radius:0 14px 14px 0;display:flex;flex-direction:column;justify-content:center}
.rule-badge{position:absolute;top:754px;width:64px;height:64px;border-radius:50%;display:flex;align-items:center;justify-content:center}
.must .rule-head{left:90px;width:275px;background:var(--green);padding-left:50px}
.must .rule-badge{left:60px;background:var(--green)}
.help .rule-head{left:510px;width:275px;background:var(--navy);padding-left:36px}
.help .rule-badge{left:480px;background:var(--navy)}
.rule-head .h{font-family:"Roboto Condensed",sans-serif;font-weight:700;color:var(--gold);font-size:17px;line-height:18px}
.rule-head .sub{font-family:"Roboto Condensed",sans-serif;color:var(--white);font-size:13px;line-height:15px}
.ai-list{position:absolute;top:818px;list-style:none}
.ai-list li{display:flex;align-items:center;gap:12px;height:32.3px;font-size:9.8px;white-space:nowrap}
.ai-list li.big{font-size:12px}
.must .ai-list{left:90px}
.help .ai-list{left:510px}

.prop{border-radius:10px}
.cannot-box{left:68px;top:1002px;width:719px;height:98px;border:1.5px solid var(--red);border-radius:14px;background:var(--white)}
.cannot-tab{left:340px;top:984px;width:240px;height:28px;background:var(--red);clip-path:polygon(0 0,100% 0,94% 100%,6% 100%);display:flex;align-items:center;justify-content:center;color:var(--white);font-family:"Roboto Condensed",sans-serif;font-weight:700;font-size:15px}
.cannot-badge{left:75px;top:985px;width:36px;height:36px}
.cannot-col{position:absolute;top:1017px;width:160px;text-align:center;font-family:"Roboto Condensed",sans-serif;font-size:12.4px;line-height:13.6px;color:var(--ink)}
.cannot-col svg{display:block;margin:0 auto 6px}
.cannot-sep{position:absolute;top:1024px;width:1px;height:76px;background:#b9bccb}

/* footer */
.foot-mark{left:74px;top:1140px;font-family:"Roboto Condensed",sans-serif;font-weight:700;color:var(--white);font-size:15px}
.foot-mark i{display:inline-block;width:12px;height:12px;background:var(--gold);margin-right:6px;vertical-align:-1px}
.foot-line1{left:133px;top:1134px;font-family:"Roboto Condensed",sans-serif;font-weight:700;font-size:14.5px;color:var(--white)}
.foot-line2{left:133px;top:1153px;font-family:"Roboto Condensed",sans-serif;font-weight:700;font-size:29px;color:var(--gold)}
</style>
</head>
<body>

<svg class="backdrop" width="848" height="1200" viewBox="0 0 848 1200" aria-hidden="true">
  <rect width="848" height="1200" fill="#f4f6fb"/>
  <path d="M0 0H120Q40 20 0 60Z" fill="#f8c220"/>
  <path d="M0 0H70Q20 10 0 30Z" fill="#0e3d86"/>
  <path d="M700 0H848V130Q830 30 700 0Z" fill="#0e3d86"/>
  <path d="M0 660Q60 690 200 690H848V640Q760 680 680 690L848 690V1200H0Z" fill="#0e3d86"/>
  <path d="M0 660Q70 700 200 690" stroke="#f8c220" stroke-width="6" fill="none"/>
  <path d="M650 700Q760 690 848 640" stroke="#f8c220" stroke-width="6" fill="none"/>
  <path d="M520 1185Q720 1175 848 1140V1165Q720 1195 520 1190Z" fill="#f8c220"/>
</svg>

<!-- header -->
<div class="abs brand">
  <div class="brand-mark"></div>
  <div class="brand-name">CALDERWOOD<br>STATE HIGH SCHOOL</div>
</div>
<div class="abs header-rule"></div>
<h1 class="abs title"><span class="line1">BEFORE YOU</span><span class="line2">ASK THE TEACHER...</span></h1>
<div class="abs deco" role="img" aria-label="Lightbulb sketch" style="left:586px;top:22px;width:56px;height:56px;background:rgba(248,194,32,.25)"></div>
<div class="abs deco" role="img" aria-label="Paper plane sketch" style="left:782px;top:132px;width:56px;height:40px;background:rgba(14,61,134,.12)"></div>
<div class="abs steps-banner"><span>TRY THESE STEPS FIRST!</span></div>

<!-- step 1 -->
<section class="card card-think" style="left:35px;width:228px">
  <div class="card-icon" style="left:117px"><div class="disc">
    <svg width="44" height="44" viewBox="0 0 44 44"><path d="M22 8a10 10 0 0 0-6 18v5h12v-5A10 10 0 0 0 22 8z" fill="#fff"/><rect x="17" y="33" width="10" height="4" rx="1" fill="#fff"/><g stroke="#f8c220" stroke-width="2"><path d="M22 1v4M6 17h4M34 17h4M10 7l3 3M34 7l-3 3"/></g><path d="M19 16h6M22 16v10" stroke="#1b2549" stroke-width="2"/></svg>
  </div></div>
  <div class="step-tab">1</div>
  <h2>THINK FIRST</h2>
  <p class="lead">Don't give up straight away.</p>
  <div class="dash"></div>
  <ul class="checklist" style="left:12px;top:133px">
    <li><svg class="tick" viewBox="0 0 24 24"><circle cx="12" cy="12" r="12" fill="#1b2549"/><path d="M7 12.5l3.3 3.3L17 9" stroke="#fff" stroke-width="2.4" fill="none"/></svg>Read the question carefully.</li>
    <li><svg class="tick" viewBox="0 0 24 24"><circle cx="12" cy="12" r="12" fill="#1b2549"/><path d="M7 12.5l3.3 3.3L17 9" stroke="#fff" stroke-width="2.4" fill="none"/></svg>Identify what you already know.</li>
    <li><svg class="tick" viewBox="0 0 24 24"><circle cx="12" cy="12" r="12" fill="#1b2549"/><path d="M7 12.5l3.3 3.3L17 9" stroke="#fff" stroke-width="2.4" fill="none"/></svg>Try a strategy you've used before.</li>
    <li><svg class="tick" viewBox="0 0 24 24"><circle cx="12" cy="12" r="12" fill="#1b2549"/><path d="M7 12.5l3.3 3.3L17 9" stroke="#fff" stroke-width="2.4" fill="none"/></svg>Give yourself thinking time.</li>
  </ul>
  <div class="card-foot">
    <svg width="26" height="34" viewBox="0 0 26 34"><path d="M5 2h16v10a8 8 0 0 1-16 0z" fill="#f8c220"/><path d="M5 5H1v3a5 5 0 0 0 5 5M21 5h4v3a5 5 0 0 1-5 5" stroke="#f8c220" stroke-width="2" fill="none"/><rect x="11" y="19" width="4" height="7" fill="#f8c220"/><rect x="6" y="26" width="14" height="6" fill="#e8a33a"/></svg>
    <span>WE BELIEVE</span>
  </div>
</section>

<!-- step 2 -->
<section class="card card-supports" style="left:310px;width:235px">
  <div class="card-icon" style="left:118px"><div class="disc">
    <svg width="52" height="48" viewBox="0 0 52 48"><circle cx="30" cy="8" r="6" fill="#f8c220"/><rect x="14" y="12" width="16" height="11" rx="2" fill="#fff"/><text x="19" y="21" font-size="9" fill="#1b2549" font-family="Roboto">?</text><rect x="28" y="16" width="18" height="11" rx="2" fill="#fff"/><path d="M32 20h10M32 23h7" stroke="#1b2549" stroke-width="1.5"/><rect x="4" y="30" width="7" height="14" fill="#fff"/><path d="M12 32h14l6 4h-10M12 42h16l18-12" stroke="#fff" stroke-width="3" fill="none"/></svg>
  </div></div>
  <div class="step-tab">2</div>
  <h2>CHECK YOUR SUPPORTS</h2>
  <p class="lead">Before asking for help, check</p>
  <div class="dash"></div>
  <ul class="checklist" style="left:12px;top:133px">
    <li><svg class="tick" viewBox="0 0 24 24"><circle cx="12" cy="12" r="12" fill="#1b2549"/><path d="M7 12.5l3.3 3.3L17 9" stroke="#fff" stroke-width="2.4" fill="none"/></svg>Learning goal and success criteria.</li>
    <li><svg class="tick" viewBox="0 0 24 24"><circle cx="12" cy="12" r="12" fill="#1b2549"/><path d="M7 12.5l3.3 3.3L17 9" stroke="#fff" stroke-width="2.4" fill="none"/></svg>Worked examples.</li>
    <li><svg class="tick" viewBox="0 0 24 24"><circle cx="12" cy="12" r="12" fill="#1b2549"/><path d="M7 12.5l3.3 3.3L17 9" stroke="#fff" stroke-width="2.4" fill="none"/></svg>Class notes.</li>
    <li><svg class="tick" viewBox="0 0 24 24"><circle cx="12" cy="12" r="12" fill="#1b2549"/><path d="M7 12.5l3.3 3.3L17 9" stroke="#fff" stroke-width="2.4" fill="none"/></svg>Classroom displays.</li>
    <li><svg class="tick" viewBox="0 0 24 24"><circle cx="12" cy="12" r="12" fill="#1b2549"/><path d="M7 12.5l3.3 3.3L17 9" stroke="#fff" stroke-width="2.4" fill="none"/></svg>LumoLearn resources.</li>
  </ul>
  <div class="card-foot">
    <svg width="38" height="34" viewBox="0 0 38 34"><circle cx="20" cy="9" r="6" fill="none" stroke="#f8c220" stroke-width="2.5"/><path d="M17 9l2 2 4-4" stroke="#f8c220" stroke-width="1.8" fill="none"/><rect x="1" y="22" width="5" height="10" fill="#f8c220"/><path d="M7 24h10l4 3h-7M7 31h12l16-9" stroke="#fff" stroke-width="2.2" fill="none"/></svg>
    <span>WE STRIVE</span>
  </div>
</section>

<!-- step 3 -->
<section class="card card-ask" style="left:570px;width:228px">
  <div class="card-icon" style="left:116px"><div class="disc">
    <svg width="60" height="48" viewBox="0 0 60 48"><ellipse cx="17" cy="16" rx="15" ry="11" fill="#fff"/><ellipse cx="43" cy="16" rx="15" ry="11" fill="#fff"/><path d="M10 13h14M10 17h14M10 21h14M36 13h14M36 17h14M36 21h14" stroke="#1b2549" stroke-width="1.8"/><circle cx="30" cy="36" r="9" fill="#f8c220"/><path d="M30 31v5l3 3" stroke="#1b2549" stroke-width="1.8" fill="none"/></svg>
  </div></div>
  <div class="step-tab">3</div>
  <h2>ASK 3 BEFORE ME</h2>
  <p class="lead">Ask three sources before<br>asking the teacher.</p>
  <div class="dash"></div>
  <ul class="checklist" style="left:12px;top:143px">
    <li><svg class="tick" viewBox="0 0 24 24"><circle cx="12" cy="12" r="12" fill="#1b2549"/><path d="M7 12.5l3.3 3.3L17 9" stroke="#fff" stroke-width="2.4" fill="none"/></svg>A person (partner or neighbour)</li>
    <li><svg class="tick" viewBox="0 0 24 24"><circle cx="12" cy="12" r="12" fill="#1b2549"/><path d="M7 12.5l3.3 3.3L17 9" stroke="#fff" stroke-width="2.4" fill="none"/></svg>A place (notes, display, LumoLearn)</li>
    <li class="tall"><svg class="tick" viewBox="0 0 24 24"><circle cx="12" cy="12" r="12" fill="#1b2549"/><path d="M7 12.5l3.3 3.3L17 9" stroke="#fff" stroke-width="2.4" fill="none"/></svg><span>A resource (worked example,<br>task sheet)</span></li>
  </ul>
  <div class="rule"></div>
  <p class="then">Then ask the teacher if<br>you still need help.</p>
  <div class="card-foot">
    <svg width="30" height="30" viewBox="0 0 30 30"><path d="M15 1l4.2 9 9.8 1.1-7.3 6.6 2 9.6L15 22.5l-8.7 4.8 2-9.6L1 11.1l9.8-1.1z" fill="#f8c220"/></svg>
    <span>WE ACHIEVE</span>
  </div>
</section>

<!-- AI section -->
<div class="abs ai-banner"></div>
<h2 class="abs ai-title"><span class="chev">«</span>USING AI AND OTHER TOOLS<span class="chev">»</span></h2>
<div class="abs ai-script">Responcibly</div>
<div class="abs ai-panel"></div>
<div class="abs ai-visual" role="img" aria-label="Robotic hand reaching toward a glowing orb"></div>

<div class="must">
  <div class="rule-box" style="left:68px"></div>
  <div class="rule-head"><span class="h">WHAT YOU MUST DO</span></div>
  <div class="rule-badge">
    <svg width="36" height="40" viewBox="0 0 36 40"><rect x="2" y="4" width="32" height="34" rx="4" fill="#fff"/><rect x="11" y="1" width="14" height="6" rx="2" fill="#fff" stroke="#246a2e" stroke-width="1.5"/><path d="M7 16l3 3 5-5M7 28l3 3 5-5" stroke="#246a2e" stroke-width="2.2" fill="none"/><path d="M19 16h10M19 20h7M19 29h10M19 33h7" stroke="#246a2e" stroke-width="2.2"/></svg>
  </div>
  <ul class="ai-list">
    <li class="big"><svg class="tick" viewBox="0 0 24 24"><circle cx="12" cy="12" r="12" fill="#246a2e"/><path d="M7 12.5l3.3 3.3L17 9" stroke="#fff" stroke-width="2.4" fill="none"/></svg>Brainstorm ideas</li>
    <li><svg class="tick" viewBox="0 0 24 24"><circle cx="12" cy="12" r="12" fill="#246a2e"/><path d="M7 12.5l3.3 3.3L17 9" stroke="#fff" stroke-width="2.4" fill="none"/></svg>Check spelling, grammar and clarity</li>
    <li><svg class="tick" viewBox="0 0 24 24"><circle cx="12" cy="12" r="12" fill="#246a2e"/><path d="M7 12.5l3.3 3.3L17 9" stroke="#fff" stroke-width="2.4" fill="none"/></svg>Read your work aloud using text-to-speech tools</li>
    <li><svg class="tick" viewBox="0 0 24 24"><circle cx="12" cy="12" r="12" fill="#246a2e"/><path d="M7 12.5l3.3 3.3L17 9" stroke="#fff" stroke-width="2.4" fill="none"/></svg>Help identify areas for improvement in a draft</li>
  </ul>
</div>

<div class="help">
  <div class="rule-box" style="left:488px"></div>
  <div class="rule-head"><span class="h">WHAT AI CAN HELP YOU DO</span><span class="sub">(WHEN APPROVED BY YOUR TEACHER)</span></div>
  <div class="rule-badge">
    <svg width="36" height="40" viewBox="0 0 36 40"><circle cx="18" cy="10" r="8" fill="none" stroke="#fff" stroke-width="2"/><text x="14.5" y="14.5" font-size="12" fill="#fff" font-family="Roboto" font-weight="700">?</text><rect x="11" y="20" width="14" height="12" rx="2" fill="none" stroke="#fff" stroke-width="2"/><path d="M11 24L5 30M25 24l6 6M14 32v6M22 32v6" stroke="#fff" stroke-width="2"/></svg>
  </div>
  <ul class="ai-list">
    <li class="big"><svg class="tick" viewBox="0 0 24 24"><circle cx="12" cy="12" r="12" fill="#0e3d86"/><path d="M7 12.5l3.3 3.3L17 9" stroke="#fff" stroke-width="2.4" fill="none"/></svg>Brainstorm ideas</li>
    <li><svg class="tick" viewBox="0 0 24 24"><circle cx="12" cy="12" r="12" fill="#0e3d86"/><path d="M7 12.5l3.3 3.3L17 9" stroke="#fff" stroke-width="2.4" fill="none"/></svg>Check spelling, grammar and clarity</li>
    <li><svg class="tick" viewBox="0 0 24 24"><circle cx="12" cy="12" r="12" fill="#0e3d86"/><path d="M7 12.5l3.3 3.3L17 9" stroke="#fff" stroke-width="2.4" fill="none"/></svg>Read your work aloud using text-to-speech tools</li>
    <li><svg class="tick" viewBox="0 0 24 24"><circle cx="12" cy="12" r="12" fill="#0e3d86"/><path d="M7 12.5l3.3 3.3L17 9" stroke="#fff" stroke-width="2.4" fill="none"/></svg>Help identify areas for improvement in a draft</li>
  </ul>
</div>

<div class="abs prop" role="img" aria-label="Stack of books with a lightbulb" style="left:12px;top:900px;width:72px;height:90px;background:linear-gradient(#f8c220 0 25%,#e9799d 25% 60%,#5fb3a8 60%)"></div>
<div class="abs prop" role="img" aria-label="Open laptop" style="left:770px;top:884px;width:72px;height:110px;background:linear-gradient(160deg,#f6b733,#7f77d6)"></div>

<div class="abs cannot-box"></div>
<div class="abs cannot-tab">WHAT YOU CANNOT DO</div>
<svg class="abs cannot-badge" viewBox="0 0 36 36"><circle cx="18" cy="18" r="17" fill="#c9161e" stroke="#fff" stroke-width="2"/><path d="M11 11l14 14M25 11L11 25" stroke="#fff" stroke-width="4"/></svg>
<div class="cannot-col" style="left:73px"><svg width="22" height="22" viewBox="0 0 22 22"><circle cx="11" cy="11" r="11" fill="#c9161e"/><path d="M7 7l8 8M15 7l-8 8" stroke="#fff" stroke-width="2.6"/></svg>Submit<br>AI-generated<br>work as<br>your own</div>
<div class="cannot-sep" style="left:241px"></div>
<div class="cannot-col" style="left:249px"><svg width="22" height="22" viewBox="0 0 22 22"><circle cx="11" cy="11" r="11" fill="#c9161e"/><path d="M7 7l8 8M15 7l-8 8" stroke="#fff" stroke-width="2.6"/></svg>Copy and paste AI<br>responses without<br>acknowledging or<br>adapting them</div>
<div class="cannot-sep" style="left:417px"></div>
<div class="cannot-col" style="left:426px"><svg width="22" height="22" viewBox="0 0 22 22"><circle cx="11" cy="11" r="11" fill="#c9161e"/><path d="M7 7l8 8M15 7l-8 8" stroke="#fff" stroke-width="2.6"/></svg>Use AI tools<br>to complete<br>the whole<br>task for you</div>
<div class="cannot-sep" style="left:594px"></div>
<div class="cannot-col" style="left:602px"><svg width="22" height="22" viewBox="0 0 22 22"><circle cx="11" cy="11" r="11" fill="#c9161e"/><path d="M7 7l8 8M15 7l-8 8" stroke="#fff" stroke-width="2.6"/></svg>Submit work that<br>does not demonstrate<br>your understanding</div>

<!-- footer -->
<div class="abs foot-mark"><i></i>CSHS</div>
<p class="abs foot-line1">If you didn't create, develop and understand it,</p>
<p class="abs foot-line2">it isn't your work.</p>
<div class="abs deco" role="img" aria-label="Lightbulb sketch" style="left:530px;top:1122px;width:58px;height:58px;background:rgba(248,194,32,.3)"></div>

</body>
</html>
```